High end boutique food product label

We are looking for a label design to be used on our range of high end food products. We don't have a design or colour scheme in mind and are interested to see what ideas are submitted.
We would like it to feel sophisticated, chic, and eye-catching.
All of our products are handmade in Australia using Australian ingredients.
The graphics for the label will need to be scaleable to be fit a variety of labels from small squat jars with labels sized 3.5cm high and 7cm wide, to tall thin bottles with labels that are 14cm high and 4.5cm wide.
We would be interested in working with the winning designer to create these different sized labels.
The label submitted for this project should be 14cm high and 4.5cm wide, it should include our logo (file supplied in .jpeg and .ai), the product name 'Extra Virgin Olive Oil' and the size '250ml'.
This is just the front label on a bottle, we are not expecting a rear label to be created currently.
You are welcome to use any fonts you think will look good but the fonts used in our logo are Allaina Medium and Bebas Kai Regular.

```html
<!DOCTYPE html>
<html lang="en">
<head>
<meta charset="utf-8">
<title>Wren &amp; Vale — Extra Virgin Olive Oil Label</title>
<link href="https://fonts.googleapis.com/css2?family=Bebas+Neue&display=swap" rel="stylesheet">
<style>
  :root {
    --canvas: #ffffff;
    --navy-deep: #0a1934;
    --navy-top: #0e2c58;
    --pearl: #ffffff;
    --pearl-shade: #cfcfcf;
    --olive-dark: #4d7a22;
    --olive-light: #b8d94a;
    --lime: #b6ea1a;
    --ink: #1e1613;
    --white: #ffffff;
  }
  html, body {
    margin: 0;
    padding: 0;
    width: 1200px;
    height: 2798px;
    overflow: hidden;
    background: var(--canvas);
  }
  .canvas {
    position: relative;
    width: 1200px;
    height: 2798px;
  }
  .label {
    position: absolute;
    width: 535px;
    height: 1700px;
    font-family: "Bebas Neue", "Arial Narrow", sans-serif;
  }
  .label--flat { left: 0; top: 920px; }
  .label--tall {
    left: 604px;
    top: 800px;
    transform: scale(1.114, 1.094);
    transform-origin: top left;
  }
  .label__art {
    position: absolute;
    inset: 0;
    width: 535px;
    height: 1700px;
  }
  .label__brand {
    position: absolute;
    left: 0;
    width: 535px;
    top: 208px;
    text-align: center;
    font-size: 104px;
    line-height: 1;
    color: var(--ink);
    letter-spacing: 2px;
  }
  .label__product {
    position: absolute;
    left: 48px;
    top: 690px;
    margin: 0;
    font-weight: 400;
    line-height: 0.86;
  }
  .label__product span { display: block; }
  .label__grade {
    font-size: 90px;
    color: var(--lime);
  }
  .label__name {
    font-size: 158px;
    color: var(--white);
  }
  .label__volume {
    position: absolute;
    left: 212px;
    top: 1585px;
    font-size: 52px;
    line-height: 1;
    color: var(--white);
  }
</style>
</head>
<body>
<main class="canvas">

  <article class="label label--flat">
    <svg class="label__art" viewBox="0 0 535 1700" xmlns="http://www.w3.org/2000/svg">
      <defs>
        <clipPath id="flat-shape">
          <path d="M0 55 Q267 -39 535 55 L535 1635 Q267 1705 0 1635 Z"/>
        </clipPath>
        <linearGradient id="flat-navy" x1="0" y1="0" x2="0" y2="1">
          <stop offset="0" stop-color="var(--navy-top)"/>
          <stop offset="0.35" stop-color="var(--navy-deep)"/>
          <stop offset="1" stop-color="var(--navy-deep)"/>
        </linearGradient>
        <linearGradient id="flat-pearl" x1="0" y1="0" x2="1" y2="0.3">
          <stop offset="0" stop-color="var(--pearl-shade)"/>
          <stop offset="0.5" stop-color="var(--pearl)"/>
          <stop offset="1" stop-color="var(--pearl-shade)"/>
        </linearGradient>
        <linearGradient id="flat-olive" x1="0" y1="1" x2="1" y2="0">
          <stop offset="0" stop-color="var(--olive-dark)"/>
          <stop offset="0.55" stop-color="#9fc832"/>
          <stop offset="1" stop-color="var(--olive-light)"/>
        </linearGradient>
      </defs>
      <g clip-path="url(#flat-shape)">
        <rect class="label__ground" width="535" height="1700" fill="url(#flat-navy)"/>
        <path class="label__swoosh" d="M0 20 L90 10 C200 110 380 170 535 220 L535 630 C380 580 150 520 0 330 Z" fill="url(#flat-pearl)"/>
        <path class="label__foliage" role="img" aria-label="Line illustration of olives and olive leaves"
              d="M535 1200 C420 1330 260 1380 150 1420 C80 1445 25 1480 0 1510 L0 1700 L535 1700 Z"
              fill="url(#flat-olive)"/>
      </g>
    </svg>
    <div class="label__brand">Wren &amp; Vale</div>
    <h1 class="label__product">
      <span class="label__grade">Extra</span>
      <span class="label__grade">Virgin</span>
      <span class="label__name">Olive</span>
      <span class="label__name">Oil</span>
    </h1>
    <div class="label__volume">250ML</div>
  </article>

  <article class="label label--tall">
    <svg class="label__art" viewBox="0 0 535 1700" xmlns="http://www.w3.org/2000/svg">
      <defs>
        <clipPath id="tall-shape">
          <path d="M0 55 Q267 -39 535 55 L535 1635 Q267 1705 0 1635 Z"/>
        </clipPath>
        <linearGradient id="tall-navy" x1="0" y1="0" x2="0" y2="1">
          <stop offset="0" stop-color="var(--navy-top)"/>
          <stop offset="0.35" stop-color="var(--navy-deep)"/>
          <stop offset="1" stop-color="var(--navy-deep)"/>
        </linearGradient>
        <linearGradient id="tall-pearl" x1="0" y1="0" x2="1" y2="0.3">
          <stop offset="0" stop-color="var(--pearl-shade)"/>
          <stop offset="0.5" stop-color="var(--pearl)"/>
          <stop offset="1" stop-color="var(--pearl-shade)"/>
        </linearGradient>
        <linearGradient id="tall-olive" x1="0" y1="1" x2="1" y2="0">
          <stop offset="0" stop-color="var(--olive-dark)"/>
          <stop offset="0.55" stop-color="#9fc832"/>
          <stop offset="1" stop-color="var(--olive-light)"/>
        </linearGradient>
      </defs>
      <g clip-path="url(#tall-shape)">
        <rect class="label__ground" width="535" height="1700" fill="url(#tall-navy)"/>
        <path class="label__swoosh" d="M0 20 L90 10 C200 110 380 170 535 220 L535 630 C380 580 150 520 0 330 Z" fill="url(#tall-pearl)"/>
        <path class="label__foliage" role="img" aria-label="Line illustration of olives and olive leaves"
              d="M535 1200 C420 1330 260 1380 150 1420 C80 1445 25 1480 0 1510 L0 1700 L535 1700 Z"
              fill="url(#tall-olive)"/>
      </g>
    </svg>
    <div class="label__brand">Wren &amp; Vale</div>
    <h2 class="label__product">
      <span class="label__grade">Extra</span>
      <span class="label__grade">Virgin</span>
      <span class="label__name">Olive</span>
      <span class="label__name">Oil</span>
    </h2>
    <div class="label__volume">250ML</div>
  </article>

</main>
</body>
</html>
```